Business Card Design

General Brief:
Varnel Works is a newly established international manufacturing company. We have a manufacturing facility in China and are in the process of building a new facility in Brazil and are expanding into Africa, the Middle East and Western markets by marketing our products through a licensee program. We use production line manufacture processes (similar to the automotive industry) to produce houses, apartments, hotels and accommodation for the resource sector. We will need to be able to differentiate between the various regions that we serve and the market we operate in.

Key Words to describe our business:
International, Global, Professional, Quality, Standard Compliant, Designful, Cost Effective, Experienced

General Brief:
We need business card designs which cater for the possibility of differentiating the various regions that we serve and the market we operate in. Also, we need a secondary typography selection which suits the primary typography used in the corporate signature (please always state which font is being applied so as to cross-check for the necessary font licenses). First print will be made for our Chinese head office and division, therefore will have the special prerequisite of featuring two distinct languages: English-speaking and Chinese. We assume that a double sided version (recto/verso) could work best in order to separate the languages—other creative interpretations, options and integrations are welcome.

Logo Symbolism:
A dot might seem to be an unassuming little thing, the first mark on the pristine sheet of paper. In this case, the dot is a beginning. But see what just happened there? The dot, an essential component in the structure of the sentence, closed it, making it a symbol of ending. Therefore, the dot is both an origination and a conclusion, encompassing all the possibilities of the universe within it, a seed full of potential and a symbol of the supreme being. The dot is also called the "bindhu," which means "drop." The bindhu is a symbol of the absolute, marked on the forehead at the position of the third eye in the place believed to be the seat of the soul. The presence of dots outside or within a symbol can signify the presence of something else. It also acts as reminder of the concept of space and all in all performs as a very positive symbol in the Varnel Works logo.

Target Market(s)

See Stationary Project

Industry/Entity Type

Accommodation

Requirements
Must have
• See Stationary Project

Logo on Stationary Project

```html
<!DOCTYPE html>
<html lang="en">
<head>
<meta charset="utf-8">
<title>Varnel Works – Business Card</title>
<link rel="stylesheet" href="https://fonts.googleapis.com/css2?family=Barlow:wght@400;500;600&display=swap">
<style>
  :root {
    --navy: #0f2334;
    --blue: #1592d9;
    --paper: #ffffff;
    --backdrop: #ececec;
    --text: #14283a;
  }
  * { margin: 0; padding: 0; box-sizing: border-box; }
  html, body {
    width: 1200px;
    height: 747px;
    overflow: hidden;
    background: var(--backdrop);
    font-family: "Barlow", Arial, sans-serif;
    color: var(--text);
  }
  .stage { position: relative; width: 1200px; height: 747px; }

  .card {
    position: absolute;
    top: 224px;
    width: 501px;
    height: 283px;
    background: var(--paper);
    overflow: hidden;
  }
  .card--front { left: 83px; }
  .card--back { left: 631px; }

  .bar { position: absolute; height: 13px; }
  .bar--navy { background: var(--navy); }
  .bar--blue { background: var(--blue); }
  .bar--top { top: 0; }
  .bar--bottom { bottom: 0; }
  .bar--wide { width: 320px; }
  .bar--short { width: 176px; }
  .bar--left { left: 0; }
  .bar--right { right: 0; }

  .company-name {
    position: absolute;
    color: var(--navy);
    font-weight: 600;
    white-space: nowrap;
    line-height: 1;
  }
  .company-name--large {
    left: 0; right: 0;
    top: 118px;
    text-align: center;
    font-size: 44px;
    letter-spacing: 0.3px;
  }
  .company-name--small {
    right: 24px;
    top: 209px;
    font-size: 19px;
  }

  .name-tab {
    position: absolute;
    right: 0;
    top: 32px;
    width: 191px;
    height: 29px;
    background: var(--blue);
    border-radius: 4px 0 0 4px;
    color: #fff;
    font-size: 19px;
    font-weight: 500;
    line-height: 29px;
    padding-left: 14px;
  }

  .icon-strip {
    position: absolute;
    left: 0;
    top: 89px;
    width: 54px;
    height: 143px;
    background: var(--blue);
    border-radius: 0 7px 7px 0;
    display: flex;
    flex-direction: column;
    justify-content: space-between;
    align-items: center;
    padding: 14px 0 12px;
  }
  .icon-strip svg { width: 13px; height: 13px; fill: none; stroke: #fff; stroke-width: 1.6; }

  .contact-list {
    position: absolute;
    left: 64px;
    top: 98px;
    list-style: none;
    font-size: 16.5px;
    font-weight: 500;
    line-height: 25px;
  }
</style>
</head>
<body>
<main class="stage">

  <section class="card card--front" aria-label="Card front">
    <div class="bar bar--navy bar--top bar--wide bar--left"></div>
    <div class="bar bar--blue bar--top bar--short bar--right"></div>
    <div class="company-name company-name--large">Varnel Works</div>
    <div class="bar bar--blue bar--bottom bar--short bar--left"></div>
    <div class="bar bar--navy bar--bottom bar--wide bar--right"></div>
  </section>

  <section class="card card--back" aria-label="Card back">
    <div class="bar bar--navy bar--top bar--wide bar--left"></div>
    <div class="bar bar--blue bar--top bar--short bar--right"></div>

    <div class="name-tab">Your Name</div>

    <div class="icon-strip" aria-hidden="true">
      <svg viewBox="0 0 14 14"><path d="M7 13s-4.5-4.6-4.5-7.6a4.5 4.5 0 0 1 9 0C11.5 8.4 7 13 7 13z"/><circle cx="7" cy="5.4" r="1.5"/></svg>
      <svg viewBox="0 0 14 14"><path d="M3 1.5l2.2 2.8-1.2 1.6c.9 1.8 2.2 3.1 4 4l1.6-1.2 2.8 2.2-1.4 1.6C6 12.2 1.8 8 1.4 2.9z"/></svg>
      <svg viewBox="0 0 14 14"><rect x="3.5" y="1" width="7" height="12" rx="1.2"/><path d="M6 11h2"/></svg>
      <svg viewBox="0 0 14 14"><rect x="1.5" y="3" width="11" height="8" rx="0.8"/><path d="M1.8 3.4L7 7.6l5.2-4.2"/></svg>
      <svg viewBox="0 0 14 14"><circle cx="7" cy="7" r="5.5"/><path d="M1.5 7h11M7 1.5c-2.2 2.8-2.2 8.2 0 11M7 1.5c2.2 2.8 2.2 8.2 0 11"/></svg>
    </div>

    <ul class="contact-list">
      <li class="contact-list__address">Your current or commercial address</li>
      <li class="contact-list__phone">00 - 00 - 00 - 00 - 00</li>
      <li class="contact-list__mobile">00 - 00 - 00 - 00 - 00</li>
      <li class="contact-list__email">info.support@yourwebsite.com</li>
      <li class="contact-list__web">www.yourwebsite.com</li>
    </ul>

    <div class="company-name company-name--small">Varnel Works</div>

    <div class="bar bar--blue bar--bottom bar--short bar--left"></div>
    <div class="bar bar--navy bar--bottom bar--wide bar--right"></div>
  </section>

</main>
</body>
</html>
```